New digital business consulting firm needs a professional Wordpress site

Lanternby Works Inc. is a new consulting firm that helps large companies with Digital Transformation. We help companies define a digital transformation strategy for improving the products, processes and customer journey using digital technology.

The website will serve three purposes:
1) Represent what the firm does.
2) Allow people to download research reports.
3) Collect email addresses from people who my be interested in using our services.

The tone of the website should be innovative and professional. The website will have only a few pages. You can see the type of content we wish to post on the current website www.lanternbyworks.example.

The website will support a book that is about to be released. The book cover is attached. However, the website does not necessarily have to match the book cover. Do not be constrained by the book cover.

Target Market(s)

Executives in large companies

Industry/Entity Type

Management Consulting

Font styles to use
Sans Serif

Requirements
Must have
• Professional and innovative, clean, cool
Nice to have
• None
Should not have
• None

```html
<!DOCTYPE html>
<html lang="en">
<head>
<meta charset="utf-8">
<title>Lanternby Works Inc. – Digital Transformation Consulting</title>
<link rel="stylesheet" href="https://fonts.googleapis.com/css2?family=Open+Sans:wght@300;400;600;700&display=swap">
<style>
:root{
  --brand-blue:#1d5a9a;
  --link-blue:#2a8ad6;
  --hero-green:#7dbb3a;
  --text-grey:#5e5e5e;
  --panel-grey:#ebebeb;
  --box-green:#5b8a2e;
  --box-edge:#a9c98a;
  --arrow-gold:#f0b323;
  --results-dark:#1c5236;
  --results-light:#2f7c4e;
  --insight-dark:#1f7c70;
  --insight-light:#5cc7b5;
  --footer-bg:#0b1019;
  --footer-bar:#070a10;
  --white:#ffffff;
}
*{box-sizing:border-box;margin:0;padding:0}
html,body{width:1200px;height:3267px;overflow:hidden}
body{position:relative;background:var(--white);font-family:"Open Sans",Arial,sans-serif;color:var(--text-grey)}
.abs{position:absolute}

/* header */
.site-header{left:0;top:0;width:1200px;height:65px;background:var(--white)}
.brand{left:148px;top:14px;font-size:28px;font-weight:600;color:var(--brand-blue);letter-spacing:-0.3px}
.main-nav{right:150px;top:24px;display:flex;gap:24px;font-size:12px;color:#666;align-items:center}
.main-nav .current{color:var(--link-blue)}

/* hero */
.hero{left:0;top:65px;width:1200px;height:377px}
.hero-photo{left:0;top:0;width:1200px;height:377px;background:linear-gradient(100deg,#c9d3dc 40%,#e8ecef 60%,#9aa7b2 80%,#d7dde2 100%)}
.hero svg{position:absolute;left:0;top:0}
.hero-title{left:70px;top:135px;width:500px;text-align:center;color:var(--white);font-size:40px;font-weight:400;line-height:1.15}
.hero-sub{left:70px;top:245px;width:500px;text-align:center;color:var(--white);font-size:14px}
.hero-btn{left:238px;top:280px;width:124px;height:42px;border:2px solid var(--white);color:var(--white);font-size:16px;display:flex;align-items:center;justify-content:center}

/* about */
.about{left:145px;top:512px;width:912px}
.about h2{font-size:28px;font-weight:400;color:var(--brand-blue);margin-bottom:4px}
.about p{font-size:14px;line-height:1.5;margin-bottom:14px}

/* photo bands */
.band{left:0;width:1200px}
.band-results{top:800px;height:333px;background:linear-gradient(120deg,var(--results-dark),var(--results-light) 55%,#3f8f5f)}
.band-insight{top:2000px;height:337px;background:linear-gradient(120deg,var(--insight-dark),var(--insight-light) 60%,#3ca596)}
.band-title{color:var(--white);font-weight:400}
.band-lede{color:var(--white);font-size:20px;letter-spacing:4px;line-height:1.7}

/* grey panels */
.panel-grey{left:0;width:1200px;background:var(--panel-grey)}
.body-copy{font-size:13px;line-height:1.85}
.body-copy p{margin-bottom:14px}

/* footer */
.site-footer{left:0;top:2718px;width:1200px;height:549px;background:var(--footer-bg)}
.footer-glow{left:0;top:0;width:1200px;height:500px;background:radial-gradient(ellipse at 650px 360px,rgba(150,130,40,.28),rgba(11,16,25,0) 60%)}
.footer-copy{left:36px;top:108px;width:350px;color:var(--white);font-size:14px;line-height:1.85}
.footer-copy p{margin-bottom:18px}
.footer-copy .book{color:var(--link-blue)}
.contact-form{left:423px;top:85px;width:355px;height:290px;border:2px solid #3a3f48;border-radius:8px;background:rgba(10,14,22,.8);padding:16px 18px}
.contact-form h3{color:#ddd;font-size:16px;font-weight:400;margin-bottom:12px}
.field{height:38px;background:#f4f4f4;font-size:10px;color:#aaa;padding:10px 10px}
.field-row{display:flex;gap:8px;margin-bottom:10px}
.field-row .field{flex:1}
.field-message{height:125px;margin-bottom:12px}
.form-foot{display:flex;justify-content:flex-end;align-items:center;gap:8px}
.captcha{color:#888;font-size:10px}
.captcha-box{width:40px;height:40px;background:#f4f4f4}
.submit{width:92px;height:42px;border:2px solid var(--link-blue);color:var(--link-blue);font-size:16px;display:flex;align-items:center;justify-content:center}
.contact-list{left:812px;top:85px;color:var(--white);font-size:15px}
.contact-item{display:flex;align-items:flex-start;gap:16px;margin-bottom:22px}
.contact-item small{font-size:11px;line-height:1.5;display:block}
.footer-bar{left:0;top:500px;width:1200px;height:49px;background:var(--footer-bar);border-top:1px solid #1b2230}
</style>
</head>
<body>

<header class="site-header abs">
  <div class="brand abs">Lanternby Works</div>
  <nav class="main-nav abs">
    <span class="current">Home</span><span>Book</span><span>Services</span><span>Download</span>
    <svg width="14" height="14" viewBox="0 0 14 14"><circle cx="8" cy="6" r="4.5" fill="none" stroke="#888" stroke-width="1.4"/><line x1="4.8" y1="9.2" x2="1" y2="13" stroke="#888" stroke-width="1.4"/></svg>
  </nav>
</header>

<section class="hero abs">
  <div class="hero-photo abs" role="img" aria-label="Photo of business consultants in a bright modern office"></div>
  <svg width="1200" height="377" viewBox="0 0 1200 377">
    <polygon points="0,0 520,0 640,150 510,377 0,377" fill="var(--brand-blue)"/>
    <polygon points="520,0 545,0 665,150 535,377 510,377 640,150" fill="var(--hero-green)"/>
  </svg>
  <h1 class="hero-title abs">Lanternby Works Inc. is a new consulting firm</h1>
  <p class="hero-sub abs">that helps large companies with Digital Transformation.</p>
  <div class="hero-btn abs">Read More</div>
</section>

<section class="about abs">
  <h2>ABOUT</h2>
  <p>We are a consulting firm that helps companies thrive in the new digital era. A third digital era is emerging and established companies are in a position to win big in the new era.</p>
  <p>The first digital era started in the mid-fifties when companies began automating transactions and continued doing so for several decades. The second era emerged as the Internet became ingrained in the late nineties and early 2000's, when companies and</p>
  <p>The third era is emerging now and is driven by such technologies as Internet of Things, machine learning, natural language processing (NLP), machine vision, and robotics. Companies are applying these technologies to revolutionize products, processes and the customer journey.</p>
</section>

<section class="band band-results abs" role="img" aria-label="Photo of hands typing on a laptop, tinted green">
  <div class="band-title abs" style="left:295px;top:160px;font-size:34px">RESUTL</div>
  <div class="band-lede abs" style="left:635px;top:163px;width:420px;text-align:center">Industry depth across all businesses we serve.</div>
</section>

<section class="panel-grey abs" style="top:1133px;height:468px">
  <div class="body-copy abs" style="left:145px;top:65px;width:435px;text-align:justify">
    <p>We help companies establish their digital vision, understand current technologies, and how to put them to business use – making products smarter, operational processes more efficient, and the customer journey easier.</p>
    <p>We also monitor what companies and doing in the area of digital and the relationship of digital initiatives and business performance. We look at the level of digital activities the company mentions in their annual reports. We then segregate the more digitally active companies (top half) from the less digitally active companies (bottom half) and compare business metrics.</p>
  </div>
  <svg class="abs" style="left:630px;top:75px" width="430" height="220" viewBox="0 0 430 220" font-family="Open Sans, Arial, sans-serif" font-size="12" font-weight="600" fill="#fff">
    <g stroke="#4d7a24" stroke-width="2" fill="none">
      <line x1="212" y1="42" x2="212" y2="62"/>
      <line x1="67" y1="62" x2="347" y2="62"/>
      <line x1="67" y1="62" x2="67" y2="80"/><line x1="347" y1="62" x2="347" y2="80"/>
      <line x1="212" y1="120" x2="212" y2="140"/>
      <line x1="87" y1="140" x2="337" y2="140"/>
      <line x1="87" y1="140" x2="87" y2="160"/><line x1="212" y1="140" x2="212" y2="160"/><line x1="337" y1="140" x2="337" y2="160"/>
    </g>
    <g fill="var(--box-green)" stroke="var(--box-edge)" stroke-width="2">
      <rect x="155" y="2" width="115" height="40" rx="5"/>
      <rect x="10" y="80" width="115" height="40" rx="5"/>
      <rect x="155" y="80" width="115" height="40" rx="5"/>
      <rect x="285" y="80" width="125" height="40" rx="5"/>
      <rect x="35" y="160" width="105" height="40" rx="5"/>
      <rect x="160" y="160" width="105" height="40" rx="5"/>
      <rect x="290" y="160" width="100" height="40" rx="5"/>
    </g>
    <g fill="var(--arrow-gold)">
      <polygon points="128,100 136,93 136,97 146,97 146,93 154,100 146,107 146,103 136,103 136,107"/>
      <polygon points="270,100 278,93 278,97 280,97 280,93 286,100 280,107 280,103 278,103 278,107"/>
    </g>
    <g text-anchor="middle">
      <text x="212" y="27">Vision</text>
      <text x="67" y="97">Digital</text><text x="67" y="112">Technologies</text>
      <text x="212" y="97">Business</text><text x="212" y="112">Uses</text>
      <text x="347" y="97">Business</text><text x="347" y="112">Outcomes</text>
      <text x="87" y="185">Products</text>
      <text x="212" y="185">Processes</text>
      <text x="340" y="177">Customer</text><text x="340" y="192">Journey</text>
    </g>
  </svg>
</section>

<section class="abs" style="left:0;top:1601px;width:1200px;height:399px">
  <svg class="abs" style="left:150px;top:72px" width="200" height="260" viewBox="0 0 200 260" font-family="Open Sans, Arial, sans-serif" font-size="9" fill="#333">
    <text x="90" y="8" font-size="12" text-anchor="middle">Market Cap Growth</text>
    <g text-anchor="end">
      <text x="28" y="34">20.0%</text><text x="28" y="54">18.0%</text><text x="28" y="74">16.0%</text><text x="28" y="94">14.0%</text><text x="28" y="114">12.0%</text><text x="28" y="134">10.0%</text><text x="28" y="154">8.0%</text><text x="28" y="174">6.0%</text><text x="28" y="194">4.0%</text><text x="28" y="214">2.0%</text><text x="28" y="234">0.0%</text>
    </g>
    <line x1="34" y1="231" x2="180" y2="231" stroke="#999"/>
    <rect x="56" y="51" width="22" height="180" fill="var(--box-green)"/>
    <rect x="118" y="123" width="22" height="108" fill="var(--box-green)"/>
    <text x="67" y="248" text-anchor="middle">Top Half</text>
    <text x="129" y="248" text-anchor="middle">Bottom Half</text>
  </svg>
  <div class="body-copy abs" style="left:385px;top:68px;width:672px">
    <p>For example, the chart below outlines that more digitally active companies (top half) achieved and average market cap growth per year of 18% form 2012 to 2015, whereas less digitally active companies (bottom half) increased market cap at an average of 12% per year.</p>
  </div>
</section>

<section class="band band-insight abs" role="img" aria-label="Photo of a hand touching a tablet screen, tinted teal">
  <div class="band-title abs" style="left:300px;top:50px;font-size:38px">Insight</div>
  <div class="band-lede abs" style="left:625px;top:48px;width:430px;text-align:justify">Ideas get better and more valuable the more widely they're shared. We regularly share our best insights on the tech and media industries we serve.</div>
</section>

<section class="panel-grey abs" style="top:2337px;height:381px">
  <svg class="abs" style="left:170px;top:60px" width="180" height="260" viewBox="0 0 180 260" font-family="Open Sans, Arial, sans-serif" font-size="9" fill="#333">
    <text x="86" y="8" font-size="11" text-anchor="middle">Market Cap Growth</text>
    <text x="86" y="22" font-size="11" text-anchor="middle">relative to Industry</text>
    <g text-anchor="end">
      <text x="20" y="50">1.0%</text><text x="20" y="80">0.5%</text><text x="20" y="110">0.0%</text><text x="20" y="140">-0.5%</text><text x="20" y="170">-1.0%</text><text x="20" y="200">-1.5%</text><text x="20" y="230">-2.0%</text>
    </g>
    <line x1="26" y1="107" x2="165" y2="107" stroke="#999"/>
    <rect x="43" y="65" width="22" height="42" fill="var(--box-green)"/>
    <rect x="105" y="107" width="22" height="60" fill="var(--box-green)"/>
    <text x="54" y="250" text-anchor="middle">Top Half</text>
    <text x="116" y="250" text-anchor="middle">Bottom Half</text>
  </svg>
  <div class="body-copy abs" style="left:385px;top:60px;width:672px;text-align:justify">
    <p>Isolating the impact of industry, since some industries increased market cap more than other industries shows that the the top half companies grew market cap about 0.7% faster than their industry counterparts and bottom half companies grew market cap 1% less than their industry counterparts.</p>
  </div>
</section>

<footer class="site-footer abs">
  <div class="footer-glow abs" role="img" aria-label="Faint golden dotted globe pattern on dark background"></div>
  <div class="footer-copy abs">
    <p>You can read about these concepts, examples, and how to move your company forward in the new digital era in our book <span class="book">Working Digital Forward</span>.</p>
    <p>Peruse the content on this site, and feel free to download some of our research. We hope you will find it useful. Would you like to have a conversation about digital and your company? Complete the contact form on the right sidebar. We love talking about how established companies can win big in the new digital era!</p>
  </div>
  <form class="contact-form abs">
    <h3>CONTACT FORM</h3>
    <div class="field-row"><div class="field">First Name</div><div class="field">Last Name</div></div>
    <div class="field-row"><div class="field">Email</div><div class="field">Organization</div></div>
    <div class="field field-message">Message</div>
    <div class="form-foot"><span class="captcha">6 + 5 =</span><div class="captcha-box"></div><div class="submit">Submit</div></div>
  </form>
  <div class="contact-list abs">
    <div class="contact-item">
      <svg width="22" height="22" viewBox="0 0 22 22"><path d="M5 2l4 4-2 3c1.5 3 3 4.5 6 6l3-2 4 4-3 3C9 19 3 13 2 5z" fill="#fff"/></svg>
      <span>+91 90000 12345</span>
    </div>
    <div class="contact-item">
      <svg width="22" height="18" viewBox="0 0 22 18"><rect x="1" y="2" width="20" height="14" fill="none" stroke="#fff" stroke-width="2"/><path d="M1 2l10 8 10-8" fill="none" stroke="#fff" stroke-width="2"/></svg>
      <span>info@lanternbyworks.example</span>
    </div>
    <div class="contact-item">
      <svg width="22" height="24" viewBox="0 0 22 24"><path d="M11 1a8 8 0 0 0-8 8c0 6 8 14 8 14s8-8 8-14a8 8 0 0 0-8-8z" fill="#fff"/><circle cx="11" cy="9" r="3" fill="var(--footer-bg)"/></svg>
      <span><small>House No. 12, Market Lane,</small><small>Near Civic Hall, India</small></span>
    </div>
  </div>
  <div class="footer-bar abs"></div>
</footer>

</body>
</html>
```